Business Card and Letterhead Design for Public Accounting Firm

Business card and letterhead design for a CPA Firm located in Orange County, CA. We're looking for a modern and professional design utilizing our existing logo. We'd like a clean "less is more" look, but also something that catches the eye. We provide a high level of service to our clients. Open to single or double sided business cards.

Additional info: color numbers on logo
Blue :
R 0
G 83
B 125

#00537D

Silver :

R 154
G 154
B 154

#9A9A9A

Target Market(s)

Businesses and individuals

Industry/Entity Type

Accounting

Contact Information for Business Card

Moss Whitfield & Danby LLP - 4827 Larkspur Vale Road, Irvine, CA 92614 - (949)731-2864 - mwdaccts.example

Font styles to use
Serif
Sans Serif
Other font styles liked:
• See font file uploaded

Colors
0054AA
0677BA
7BADD7
CADEEF
E8F1F8

Requirements
Nice to have
• Possibly use the font file provided which matches our logo, but adjust to be not in all caps

```html
<!DOCTYPE html>
<html lang="en">
<head>
<meta charset="utf-8">
<title>Moss Whitfield &amp; Danby LLP – Business Card</title>
<link rel="stylesheet" href="https://fonts.googleapis.com/css2?family=Cinzel:wght@400;500&family=Poppins:wght@400;500&display=swap">
<style>
  :root {
    --brand-blue: #00537d;
    --brand-silver: #9a9a9a;
    --paper: #ffffff;
    --ink-grey: #555555;
    --stage: #d4d4d4;
  }
  * { margin: 0; padding: 0; box-sizing: border-box; }
  html, body { width: 1200px; height: 800px; overflow: hidden; }
  body {
    background: var(--stage);
    display: flex;
    align-items: center;
    justify-content: center;
    gap: 40px;
  }
  .card {
    position: relative;
    width: 540px;
    height: 310px;
    border-radius: 20px;
    overflow: hidden;
    box-shadow: 0 10px 28px rgba(0,0,0,0.22);
  }
  /* Front */
  .card-front { background: var(--paper); }
  .holder { position: absolute; left: 36px; top: 44px; }
  .holder-name {
    font-family: "Cinzel", serif;
    font-size: 26px;
    font-weight: 500;
    color: var(--brand-blue);
    letter-spacing: 1px;
    line-height: 1.1;
  }
  .holder-title {
    font-family: "Poppins", sans-serif;
    font-size: 15px;
    color: var(--ink-grey);
  }
  .address-band {
    position: absolute;
    left: 0; top: 122px;
    width: 330px; height: 96px;
    background: var(--brand-blue);
    color: var(--paper);
    font-family: "Poppins", sans-serif;
    font-size: 14.5px;
    font-weight: 500;
    line-height: 1.3;
    padding: 13px 0 0 36px;
  }
  .contact-list {
    position: absolute;
    left: 36px; top: 232px;
    list-style: none;
    font-family: "Poppins", sans-serif;
    font-size: 16px;
    color: var(--ink-grey);
    line-height: 1.55;
  }
  .contact-list li { display: flex; align-items: center; gap: 10px; }
  .contact-list svg { width: 15px; height: 15px; flex: none; }
  .contact-list .web { color: var(--brand-blue); }
  .accent-square {
    position: absolute;
    right: 0; top: 34px;
    width: 78px; height: 62px;
    background: var(--brand-silver);
  }
  .front-wordmark {
    position: absolute;
    left: 352px; top: 110px;
    font-family: "Cinzel", serif;
    font-size: 52px;
    font-weight: 400;
    color: var(--brand-blue);
    letter-spacing: 1px;
  }
  /* Back */
  .card-back {
    background: var(--brand-blue);
    color: var(--paper);
    display: flex;
    align-items: center;
    justify-content: center;
    gap: 16px;
  }
  .back-wordmark {
    font-family: "Cinzel", serif;
    font-size: 46px;
    font-weight: 400;
  }
  .back-divider { width: 1px; height: 64px; background: var(--paper); }
  .back-firm {
    font-family: "Cinzel", serif;
    font-size: 16px;
    letter-spacing: 3px;
    line-height: 1.35;
  }
</style>
</head>
<body>
  <section class="card card-front" aria-label="Business card front">
    <div class="holder">
      <p class="holder-name">ELLIOT MARSH</p>
      <p class="holder-title">Managing Director</p>
    </div>
    <div class="address-band">
      <p>Moss Whitfield &amp; Danby LLP</p>
      <p>4827 Larkspur Vale Road,</p>
      <p>Irvine, CA 92614</p>
    </div>
    <ul class="contact-list">
      <li>
        <svg viewBox="0 0 16 16" aria-hidden="true"><path fill="#00537d" d="M3.6 1.5l2.3 2.6-1.3 1.7c.8 1.9 2.2 3.3 4.1 4.1l1.7-1.3 2.6 2.3-1.3 2.4C7.3 13.3 2.7 8.7 2.7 2.8z"/></svg>
        <span>(949)731-2864</span>
      </li>
      <li>
        <svg viewBox="0 0 16 16" aria-hidden="true"><circle cx="8" cy="8" r="6.5" fill="none" stroke="#00537d" stroke-width="1.5"/><ellipse cx="8" cy="8" rx="2.8" ry="6.5" fill="none" stroke="#00537d" stroke-width="1.2"/><path d="M1.5 8h13M2.6 4.8h10.8M2.6 11.2h10.8" stroke="#00537d" stroke-width="1.1"/></svg>
        <span class="web">www.mwdaccts.example</span>
      </li>
    </ul>
    <div class="accent-square"></div>
    <p class="front-wordmark">MW&amp;D</p>
  </section>

  <section class="card card-back" aria-label="Business card back">
    <p class="back-wordmark">MW&amp;D</p>
    <span class="back-divider"></span>
    <p class="back-firm">MOSS WHITFIELD<br>&amp; DANBY LLP</p>
  </section>
</body>
</html>
```